Marrowgate Auctions Business Cards Design Needed

I need a business card design that is modern looking - double sided (maybe just my logo on the back, but open to suggestions) - the overall design is up to you. I want it to be easy to read - not over the top flashy. I already have a company logo which I uploaded so that needs to be used. The colors of my logo are the colors I want on the card... so blue and gray (do need to match the logo colors).

Requirements
Must have
• Would like the card to be sleek, modern and easy to ready

```html
<!DOCTYPE html>
<html lang="en">
<head>
<meta charset="utf-8">
<title>Marrowgate Auctions – Business Cards</title>
<link href="https://fonts.googleapis.com/css2?family=Michroma&family=Roboto:wght@400;500&display=swap" rel="stylesheet">
<style>
  :root {
    --backdrop: #3b3c3e;
    --card: #1d1e20;
    --card-emboss: #35363a;
    --brand-blue: #4d8fc8;
    --mark-gray: #e6e6e6;
    --text-light: #ffffff;
  }
  html, body {
    margin: 0;
    padding: 0;
    overflow: hidden;
  }
  .canvas {
    position: relative;
    width: 799px;
    height: 1200px;
    background: var(--backdrop);
    overflow: hidden;
  }
  .card {
    position: absolute;
    left: 50px;
    width: 700px;
    height: 400px;
    background: var(--card);
    border-radius: 4px;
    overflow: hidden;
    box-shadow: 0 10px 30px rgba(0,0,0,0.35);
  }
  .card--front { top: 110px; }
  .card--back { top: 690px; }

  /* Front */
  .front-brand {
    position: absolute;
    inset: 0;
    display: flex;
    flex-direction: column;
    align-items: center;
    justify-content: center;
    gap: 22px;
  }
  .front-brand__square {
    width: 110px;
    height: 110px;
    background: var(--card-emboss);
  }
  .front-brand__name {
    font-family: "Michroma", sans-serif;
    font-size: 28px;
    letter-spacing: 1px;
    color: var(--card-emboss);
    text-transform: uppercase;
    white-space: nowrap;
  }

  /* Back */
  .back-band {
    position: absolute;
    inset: 0;
  }
  .back-square {
    position: absolute;
    left: 70px;
    top: 70px;
    width: 170px;
    height: 170px;
    background: var(--mark-gray);
  }
  .back-wordmark {
    position: absolute;
    right: 40px;
    top: 48px;
    margin: 0;
    font-family: "Michroma", sans-serif;
    font-size: 26px;
    line-height: 1.3;
    color: var(--mark-gray);
    text-transform: uppercase;
    letter-spacing: 0.5px;
    text-align: right;
  }
  .back-wordmark span { display: block; white-space: nowrap; }
  .contact {
    position: absolute;
    right: 40px;
    top: 178px;
    text-align: right;
    font-family: "Roboto", sans-serif;
    color: var(--text-light);
  }
  .contact__name {
    font-family: "Michroma", sans-serif;
    font-size: 22px;
    margin: 0 0 2px;
  }
  .contact__title {
    font-size: 15px;
    margin: 0 0 14px;
  }
  .contact__line {
    display: flex;
    justify-content: flex-end;
    align-items: center;
    gap: 10px;
    font-size: 16px;
    margin: 3px 0;
  }
  .contact__line svg {
    width: 15px;
    height: 15px;
    fill: var(--text-light);
  }
  .tagline {
    position: absolute;
    left: 40px;
    bottom: 26px;
    font-family: "Roboto", sans-serif;
    font-size: 15px;
    letter-spacing: 0.5px;
    color: var(--brand-blue);
    text-transform: uppercase;
  }
</style>
</head>
<body>
<main class="canvas">

  <section class="card card--front" aria-label="Card front">
    <div class="front-brand">
      <div class="front-brand__square"></div>
      <div class="front-brand__name">Marrowgate Auctions</div>
    </div>
  </section>

  <section class="card card--back" aria-label="Card back">
    <svg class="back-band" width="700" height="400" viewBox="0 0 700 400" aria-hidden="true">
      <rect x="36" y="70" width="16" height="170" fill="var(--brand-blue)"/>
      <polygon points="250,160 700,160 700,330 180,330" fill="var(--brand-blue)"/>
    </svg>
    <div class="back-square"></div>
    <p class="back-wordmark"><span>Marrowgate</span><span>Auctions</span></p>

    <div class="contact">
      <p class="contact__name">Colin Hartwell</p>
      <p class="contact__title">Owner/President - Auctioneer</p>
      <p class="contact__line">555-014-2290
        <svg viewBox="0 0 24 24"><path d="M6.6 10.8a15 15 0 0 0 6.6 6.6l2.2-2.2a1 1 0 0 1 1-.25 11.4 11.4 0 0 0 3.6.57 1 1 0 0 1 1 1V20a1 1 0 0 1-1 1A17 17 0 0 1 3 4a1 1 0 0 1 1-1h3.5a1 1 0 0 1 1 1c0 1.25.2 2.45.57 3.57a1 1 0 0 1-.25 1z"/></svg>
      </p>
      <p class="contact__line">hello@marrowgateauctions.com
        <svg viewBox="0 0 24 24"><path d="M2 5h20v14H2z M4 7v.5l8 5 8-5V7l-8 5z" fill-rule="evenodd"/></svg>
      </p>
      <p class="contact__line">www.bidrevival.com
        <svg viewBox="0 0 24 24"><circle cx="12" cy="12" r="9" fill="none" stroke="#fff" stroke-width="2"/><path d="M3 12h18M12 3c3 3 3 15 0 18M12 3c-3 3-3 15 0 18" fill="none" stroke="#fff" stroke-width="1.6"/></svg>
      </p>
    </div>

    <div class="tagline">Improving charity auctions nationwide</div>
  </section>

</main>
</body>
</html>
```